Flyer for customer acquisition.

Hello, We are a sportmanagement agency from Germany and we need information flyers for customer acquisition. It should be DinA4 and should have a modern but serious design. I have uploaded a information sheet, where you can find the text and the composition, the flyer should have. I also uploaded Pictures / Images, which you can use. Of course you can use other suitable images. If they are not free, I will buy them later. On the bottom of the flyer there has been the contact information. You will find them in the download section, too. If you have questions, just write me. If I forgot something, I will update the letter :) Thank you very much!
Ich brauche zusätzliche Tage um durchzusehen

```html
<!DOCTYPE html>
<html lang="de">
<head>
<meta charset="utf-8">
<title>BRX-T Nachwuchsförderung – Flyer</title>
<link href="https://fonts.googleapis.com/css2?family=Roboto+Condensed:wght@400;700&family=PT+Sans:wght@400;700&display=swap" rel="stylesheet">
<style>
  :root{
    --blue:#2f5d91;
    --blue-bar:#3d6897;
    --ink:#2b2b2b;
    --frame:#555;
    --black:#1f1f1f;
    --sky-top:#8fb8e3;
    --sky-mid:#d6e7f6;
    --grass:#8cc63f;
    --grass-dark:#5f9e22;
    --page:#ececec;
  }
  *{box-sizing:border-box;margin:0;padding:0}
  html,body{width:1200px;height:1120px;overflow:hidden;background:var(--page)}
  .flyer{
    position:absolute;left:218px;top:20px;width:763px;height:1080px;
    background:#fff;overflow:hidden;box-shadow:0 4px 18px rgba(0,0,0,.25);
    font-family:"PT Sans",sans-serif;color:var(--ink);
  }
  .sky{position:absolute;left:0;top:0;width:100%;height:710px;
    background:linear-gradient(180deg,var(--sky-top) 0%,var(--sky-mid) 25%,#f4f8fb 55%,#fff 75%,#e6e6e6 100%)}
  .title{position:absolute;left:0;width:100%;text-align:center;
    font-family:"Roboto Condensed",sans-serif;font-weight:700;color:var(--blue);
    font-size:45px;line-height:1;letter-spacing:.2px}
  .title.l1{top:34px}
  .title.l2{top:88px}
  .claim{position:absolute;left:160px;top:134px;width:442px;height:36px;background:var(--black);
    color:#fff;font-family:"Roboto Condensed",sans-serif;font-size:23px;line-height:36px;text-align:center}
  .box{position:absolute;border:1px solid var(--frame);background:rgba(255,255,255,.6);padding:3px 9px 3px 9px;overflow:hidden}
  .box h3{font-family:"Roboto Condensed",sans-serif;font-weight:400;font-size:12.5px;color:var(--blue);line-height:15px;margin-bottom:2px}
  .box p{font-size:12px;line-height:15px;text-align:justify}
  .contact{position:absolute;left:76px;top:658px;width:610px;height:52px;background:var(--blue-bar);
    border-radius:14px 14px 0 0;display:flex;align-items:center;justify-content:center;gap:30px;
    font-family:"Roboto Condensed",sans-serif;color:#fff;font-size:22px}
  .contact span{display:flex;align-items:center;gap:7px}
  .contact svg{width:17px;height:17px}
  .field{position:absolute;left:0;top:710px;width:100%;height:230px;
    background:linear-gradient(180deg,var(--grass) 0%,#a9d66a 55%,#e3f1cf 85%,#fff 100%)}
  .pieces{position:absolute;left:112px;top:80px;width:520px;height:190px;
    background:radial-gradient(ellipse at center,var(--grass-dark) 0%,rgba(95,158,34,.6) 55%,rgba(95,158,34,0) 75%)}
  .brand{position:absolute;left:57px;top:975px;width:246px;display:flex;align-items:center;justify-content:center;gap:10px;
    font-family:"PT Sans",sans-serif;font-weight:700;font-size:34px;color:var(--black)}
  .brand i{display:block;width:18px;height:18px;border-radius:50%;background:var(--black)}
  .notes{position:absolute;left:341px;top:970px;width:386px;font-size:9.5px;line-height:12.5px;text-align:justify}
  .notes p+p{margin-top:12px}
</style>
</head>
<body>
<main class="flyer">
  <div class="sky"></div>
  <h1 class="title l1">BRX-T NACHWUCHSFÖRDERUNG</h1>
  <h1 class="title l2">UND -MANGEMENT</h1>
  <div class="claim">Wir begleiten dich auf deinem Weg zum Profi</div>

  <section class="box" style="left:37px;top:192px;width:424px;height:72px">
    <h3>KARRIEREPLANUNG</h3>
    <p>Wir haben deine Karriere im Blick! In enger Absprache mit deinen Eltern und dir leiten wir die richtigen Maßnahmen und Schritte ein, um dein Ziel „Profifußballer“ zu realisieren.</p>
  </section>
  <div class="box" style="left:465px;top:192px;width:260px;height:72px"></div>

  <section class="box" style="left:37px;top:269px;width:424px;height:71px">
    <h3>STÄNDIGER ANSPRECHPARTNER</h3>
    <p>Egal um welchen Themen es sich handelt, wir sind für dich da! Ein vertrauensvolles und freundschaftliches Verhältnis ist uns besonders wichtig.</p>
  </section>
  <div class="box" style="left:465px;top:269px;width:260px;height:71px"></div>

  <section class="box" style="left:37px;top:344px;width:424px;height:66px">
    <h3>RECHTSBERATUNG/VERTRAGSRECHT</h3>
    <p>Juristendeutsch und Kleingedrucktes? Kein Problem! Wir helfen dir den Durchblick zu behalten und holen immer das Beste für dich raus.</p>
  </section>
  <div class="box" style="left:465px;top:344px;width:260px;height:66px"></div>

  <div class="box" style="left:37px;top:422px;width:260px;height:66px"></div>
  <section class="box" style="left:302px;top:422px;width:423px;height:66px">
    <h3>AUSRÜSTUNG</h3>
    <p>Wir besorgen dir deine Ausrüstung! Unsere Beziehungen zu den großen Sportartikelherstellern ermöglichen den Abschluss von Ausrüsterverträgen*.</p>
  </section>

  <div class="box" style="left:37px;top:492px;width:260px;height:53px"></div>
  <section class="box" style="left:302px;top:492px;width:423px;height:53px">
    <h3>VORSORGE</h3>
    <p>Verletzungen gehören leider zum Fußball dazu. Wir sichern dich ab, indem wir eine private Zusatzkrankenversicherung für dich abschließen.</p>
  </section>

  <div class="box" style="left:37px;top:549px;width:260px;height:77px"></div>
  <section class="box" style="left:302px;top:549px;width:423px;height:77px">
    <h3>KOOPERATIONSPARTNER/NETZWERK</h3>
    <p>Ob Entscheidungsträger oder Experte, wir kennen die richtigen Leute. Zusätzlich bieten wir dir eine große Bandbreite an Leistungen, die du jederzeit in Anspruch nehmen kannst**.</p>
  </section>

  <div class="field" role="img" aria-label="Gestreifter Fußballrasen mit einer Reihe Schachfiguren aus Gras">
    <div class="pieces"></div>
  </div>

  <nav class="contact">
    <span><svg viewBox="0 0 16 16"><rect x="4" y="1" width="8" height="14" rx="1.5" fill="none" stroke="#fff" stroke-width="1.6"/><circle cx="8" cy="12.5" r=".9" fill="#fff"/></svg>01234/5678900</span>
    <span><svg viewBox="0 0 16 16"><rect x="1" y="4" width="14" height="9" fill="none" stroke="#fff" stroke-width="1.5"/><path d="M1 4l7 5 7-5" fill="none" stroke="#fff" stroke-width="1.5"/></svg>info@brx-t.de</span>
    <span><svg viewBox="0 0 16 16"><circle cx="8" cy="8" r="6.5" fill="none" stroke="#fff" stroke-width="1.4"/><ellipse cx="8" cy="8" rx="2.8" ry="6.5" fill="none" stroke="#fff" stroke-width="1.2"/><path d="M1.5 8h13M3 4.5h10M3 11.5h10" stroke="#fff" stroke-width="1.1"/></svg>www.brx-t.de</span>
  </nav>

  <div class="brand"><i></i>BRX-T</div>

  <div class="notes">
    <p>*Die Entscheidung über das Zustandekommen eines Ausrüstervertrags obliegt dem jeweiligen Sportartikelhersteller. Ist ein Abschluss aktuell nicht möglich, erhältst du von uns 2x pro Saison neue Fußballschuhe sowie weitere Ausrüstungsgegenstände.</p>
    <p>**Personal Training, Athletik-Training, Ernährungsberatung, Sportpsychologische Betreuung, uvm.</p>
  </div>
</main>
</body>
</html>
```